Cultured Basics Website Design

We need a modern, elegant website for a nutritional product called "Cultured Basics" which is based on the diets of people living in Longevity Hot Spots. In Longevity Hot Spots people live uncommonly longer and healthier lives. Most of these Hot Spots are in exotic locations around the world. I have attached several images taken from the Hot Spot in Costa Rica, along with our Logo and the text for the entire website. It is not necessary to use/include all of the text, we can add and adjust that later. For now, we need the design for the home page and template for interior pages. You do not have to use the images we provide, we can purchase additional images if needed. "Final selection should include Adobe Muse template file and all supporting graphics in editable formats (PhotoShop, Illustrator, etc)" We have posted several projects on Sketch Harbor and have accepted in every case. We look forward to seeing your design for our website. Thanks!
We like the look of these websites as an example. You have to press "Preview" (which is located on the right) to see the website.
https://www.pagebloomer.com/websites/templates/drift
https://www.pagebloomer.com/websites/templates/marlow
35-60 80% female, 20% male
Product
1 page

```html
<!DOCTYPE html>
<html lang="en">
<head>
<meta charset="utf-8">
<title>Cultured Basics</title>
<link href="https://fonts.googleapis.com/css2?family=Montserrat:wght@600;700;800&family=Raleway:wght@400;500;600;700&display=swap" rel="stylesheet">
<style>
:root{
  --ink:#111111;
  --black:#000000;
  --white:#ffffff;
  --leaf:#7cc242;
  --body:#222222;
  --muted:#c9c9c9;
  --dark-section:#2b2b27;
  --field:#ffffff;
  --field-btn:#d8d8d8;
}
*{box-sizing:border-box;margin:0;padding:0}
html,body{width:1200px;height:3130px;overflow:hidden;background:var(--white)}
body{position:relative;font-family:"Raleway",sans-serif;color:var(--body)}
.abs{position:absolute}

/* header */
.site-header{left:0;top:0;width:1200px;height:94px;background:var(--black)}
.brand{left:40px;top:22px;display:flex;align-items:center;gap:10px;color:var(--leaf);font-family:"Raleway",sans-serif;font-weight:700;font-size:27px;line-height:1}
.brand-dot{width:16px;height:16px;border-radius:50%;background:var(--leaf)}
.main-nav{top:0;height:94px;display:flex;align-items:center}
.main-nav a{position:absolute;color:var(--white);text-decoration:none;font-family:"Montserrat",sans-serif;font-weight:700;font-size:16px;letter-spacing:.5px;white-space:nowrap}
.search-icon{left:1138px;top:38px}

/* hero */
.hero{left:0;top:94px;width:1200px;height:556px;background:linear-gradient(180deg,#6fa9d8 0%,#a9cde6 45%,#bcd3d6 62%,#d9ccb2 78%,#cdbb98 100%)}
.hero-title{left:0;top:296px;width:1190px;text-align:center;color:var(--white);font-family:"Montserrat",sans-serif;font-weight:700;font-size:52px;line-height:60px;letter-spacing:1px}
.hero-btn{left:535px;top:430px;width:130px;height:42px;background:var(--ink);color:var(--white);font-family:"Montserrat",sans-serif;font-weight:700;font-size:12px;display:flex;align-items:center;justify-content:center;letter-spacing:.5px}

/* intro */
.intro{left:228px;top:698px;width:740px;text-align:center;font-size:16.5px;line-height:22px;color:var(--body)}
.divider-x{width:30px;height:30px}

/* carousel */
.slide{background:linear-gradient(160deg,#5d7a3a,#8d6a47 60%,#b29a7a)}
.slide-side{opacity:.45}
.slide-arrow{top:1036px}

/* story */
.story{left:0;top:1484px;width:1200px;height:820px;background:radial-gradient(ellipse at 72% 55%,#4a4a42 0%,#333330 45%,#222220 100%)}
.story-text{left:60px;top:1680px;width:530px;font-size:14.6px;line-height:18.3px;color:var(--muted)}

/* features */
.features-title{left:0;top:2380px;width:1200px;text-align:center;font-family:"Montserrat",sans-serif;font-weight:800;font-size:42px;color:var(--ink);letter-spacing:1px}
.feature{top:2528px;width:240px;height:162px}

/* footer */
.site-footer{left:0;top:2792px;width:1200px;height:338px;background:var(--black);color:var(--white)}
.footer-col{top:2852px}
.footer-col h4{font-family:"Montserrat",sans-serif;font-weight:700;font-size:14px;margin-bottom:14px;letter-spacing:.3px}
.footer-col li{list-style:none;font-size:11px;line-height:26px;color:#e6e6e6}
.newsletter-field{left:835px;top:2888px;width:188px;height:37px;display:flex}
.newsletter-field span{flex:1;background:var(--field);color:#555;font-size:11px;display:flex;align-items:center;padding-left:10px}
.newsletter-field b{width:50px;background:var(--field-btn);color:var(--ink);font-family:"Montserrat",sans-serif;font-size:11px;display:flex;align-items:center;justify-content:center}
.social{left:835px;top:2974px;display:flex;gap:21px}
.social i{width:14px;height:14px;border-radius:50%;background:var(--white);display:block}
.copyright{left:190px;top:3066px;font-size:11px;color:#e6e6e6}
.region{left:918px;top:3066px;font-size:11px;color:#e6e6e6;display:flex;align-items:center;gap:8px}
.region i{width:12px;height:8px;background:#c33;display:block}
</style>
</head>
<body>

<header class="abs site-header">
  <div class="abs brand"><span class="brand-dot"></span>Cultured Basics</div>
  <nav class="abs main-nav">
    <a style="left:282px">SHOP</a>
    <a style="left:360px">TEAM</a>
    <a style="left:438px">EVENTS</a>
    <a style="left:535px">EXPERIENCE</a>
    <a style="left:668px">COMPANY</a>
    <a style="left:790px">CONTACT</a>
  </nav>
  <svg class="abs search-icon" width="18" height="18" viewBox="0 0 18 18"><circle cx="7" cy="7" r="5" fill="none" stroke="#fff" stroke-width="2"/><line x1="11" y1="11" x2="16" y2="16" stroke="#fff" stroke-width="2.4"/></svg>
</header>

<section class="abs hero" role="img" aria-label="Tropical beach with palm trees, rocky headland and ocean under a blue sky"></section>
<h1 class="abs hero-title">NATURALLY ENHANCED<br>SUPERFOODS</h1>
<div class="abs hero-btn">SEE DETAILS</div>

<p class="abs intro">The healthiest people on earth eat consume a diet that is quite different from ours including a great deal of fermented foods, a variety of superfoods and probiotics. Cultured Basics helps bridge the gap between their diet and ours.</p>
<svg class="abs divider-x" style="left:585px;top:791px" viewBox="0 0 30 30"><path d="M4 4L26 26M26 4L4 26" stroke="#111" stroke-width="3"/></svg>

<div class="abs slide slide-side" style="left:0;top:913px;width:235px;height:363px" role="img" aria-label="Girls in traditional white dresses"></div>
<div class="abs slide" style="left:269px;top:864px;width:644px;height:427px" role="img" aria-label="Woman in a sun hat standing beside an elderly man in a garden"></div>
<div class="abs slide slide-side" style="left:947px;top:913px;width:253px;height:363px" role="img" aria-label="Elderly man in a hat by a pool"></div>
<svg class="abs slide-arrow" style="left:85px" width="100" height="120" viewBox="0 0 100 120"><path d="M95 5L10 60L95 115" fill="none" stroke="#888" stroke-width="5"/></svg>
<svg class="abs slide-arrow" style="left:1010px" width="100" height="120" viewBox="0 0 100 120"><path d="M5 5L90 60L5 115" fill="none" stroke="#888" stroke-width="5"/></svg>

<section class="abs story" role="img" aria-label="Two young women sitting on a wooden bench outdoors at dusk"></section>
<p class="abs story-text">For thousands of years in remote areas scattered across the globe, a handful of cultures have mastered the art of living well. In these extraordinary places, diseases are rare, sickness is infrequent and life expectancies of go to 100 plus years are common. These are commonly referred to as Longevity Hot Spots. While researching the diets of these remarkably healthy people, we made an amazing discovery that has a profound impact on health. People in Longevity Hot Spots consume fermented foods on a daily basis. Fermentation is a process our ancestors used to store and preserve food such as pickles, yogurt, sauerkraut or miso but has become a lost art in our modern world and has disappeared from our diet. Consuming fermented food nurtures digestive function and substantially benefits overall health. Fermentation predigests food and makes key nutritional components easier for our digestive systems to process, maximizing our food's nutritional benefit. Fermentation rids our food of antinutrients, harmful bacteria and other factors which inhibit nutrient absorption. It increases the bioavailability of our food by unlocking vitamin, minerals, amino acids and carbohydrates. Fermentation also improves gastrointestinal health by balancing and building a strong internal microbiome. The dual benefits of fermentation improves both the nutritional quality of our food as well as our digestive environment.</p>

<h2 class="abs features-title">FEATURES</h2>
<svg class="abs divider-x" style="left:585px;top:2450px" viewBox="0 0 30 30"><path d="M4 4L26 26M26 4L4 26" stroke="#111" stroke-width="3"/></svg>
<div class="abs feature" style="left:99px;background:linear-gradient(180deg,#a9b8c4,#5e7a52)" role="img" aria-label="Hillside house overlooking a bay"></div>
<div class="abs feature" style="left:357px;background:linear-gradient(180deg,#b8c7d2,#4f6a3c)" role="img" aria-label="Small blue house among trees"></div>
<div class="abs feature" style="left:610px;background:linear-gradient(180deg,#9fb6c6,#8a8a64)" role="img" aria-label="Rural dirt road lined with trees"></div>
<div class="abs feature" style="left:866px;background:linear-gradient(180deg,#6d7892,#c08860 60%,#3a3430)" role="img" aria-label="Boat on the beach at sunset"></div>

<footer class="abs site-footer"></footer>
<div class="abs footer-col" style="left:190px;color:#fff"><h4>PRODUCTS</h4><ul><li>Mens</li><li>Womens</li><li>Youth</li></ul></div>
<div class="abs footer-col" style="left:399px;color:#fff"><h4>ABOUT</h4><ul><li>Careers and Internships</li><li>Sponsorships</li><li>Team</li><li>Catalog Request/Download</li></ul></div>
<div class="abs footer-col" style="left:608px;color:#fff"><h4>CUSTOMER SUPPORT</h4><ul><li>Contact Us</li><li>Shipping and Order Tracking</li><li>Easy Returns</li><li>Warranty</li><li>Replacement Binding Parts</li></ul></div>
<div class="abs footer-col" style="left:835px;color:#fff"><h4>NEWSLETTER</h4></div>
<div class="abs newsletter-field"><span>Enter your email</span><b>GO</b></div>
<div class="abs social"><i></i><i></i><i></i><i></i><i></i><i></i></div>
<div class="abs copyright">© 2014 Ridgeline Boards</div>
<div class="abs region"><i></i>Change Region</div>

</body>
</html>
```